Potential SF Gazette Best Seller Poetry Book Cover Contest

I’m penning my first poetry book. It’s entitled “Lanterns Under Rain”
I’m fairly open to creative freedom but I want the cover to without a doubt catch a persons' eye instantly because first impressions are VERY IMPORTANT in the literary world
I tend to lean towards a luxury look and colors like black, gold, rose gold, silver, glitter etc but again I’m open to interpretation
Looking forward to your submissions
Target Market(s)
those seeking relatable love advice and quotes
modern millenials
Colors
Look and feel

```html
<!DOCTYPE html>
<html lang="en">
<head>
<meta charset="utf-8">
<title>Lanterns Under Rain — Book Cover</title>
<link href="https://fonts.googleapis.com/css2?family=Archivo:wght@900&family=Crimson+Text:wght@400&family=Lato:wght@300&display=swap" rel="stylesheet">
<style>
  :root {
    --cover-black: #000000;
    --title-white: #ffffff;
    --rose-ink: #b86e78;
    --badge-gold: #fcc419;
    --author-grey: #a9a9a9;
  }
  html, body {
    margin: 0;
    padding: 0;
    overflow: hidden;
    background: var(--cover-black);
  }
  .cover {
    position: relative;
    width: 900px;
    height: 1200px;
    background: var(--cover-black);
    overflow: hidden;
  }
  .title-lines {
    position: absolute;
    left: 98px;
    top: 70px;
    margin: 0;
    font-family: "Archivo", Arial, sans-serif;
    font-weight: 900;
    font-size: 112px;
    line-height: 116px;
    letter-spacing: -1px;
    color: var(--title-white);
    text-transform: uppercase;
  }
  .title-lines span { display: block; }
  .ink-art {
    position: absolute;
    left: 0;
    top: 0;
    width: 900px;
    height: 1200px;
  }
  .ink-word {
    font-family: "Archivo", Arial, sans-serif;
    font-weight: 900;
    fill: var(--rose-ink);
  }
  .author {
    position: absolute;
    left: 36px;
    top: 1096px;
    text-align: center;
  }
  .author-name {
    font-family: "Crimson Text", "Times New Roman", serif;
    font-size: 37px;
    color: var(--title-white);
    line-height: 1;
  }
  .author-role {
    margin-top: 4px;
    font-family: "Lato", Arial, sans-serif;
    font-weight: 300;
    font-size: 18px;
    color: var(--author-grey);
  }
  .bestseller-badge {
    position: absolute;
    left: 648px;
    top: 946px;
    width: 208px;
    height: 208px;
  }
</style>
</head>
<body>
<main class="cover">
  <h1 class="title-lines" aria-label="Lanterns Under Rain">
    <span>Lanterns</span>
    <span>Under</span>
  </h1>

  <svg class="ink-art" viewBox="0 0 900 1200">
    <defs>
      <linearGradient id="inkWash" x1="0" y1="0" x2="0" y2="1">
        <stop offset="0" stop-color="var(--rose-ink)"/>
        <stop offset="0.7" stop-color="var(--rose-ink)"/>
        <stop offset="1" stop-color="var(--cover-black)"/>
      </linearGradient>
    </defs>
    <text class="ink-word" x="116" y="690" font-size="400" textLength="688" lengthAdjust="spacingAndGlyphs">RAIN</text>
    <rect role="img" aria-label="Rose ink splash band across the lower cover"
      x="0" y="632" width="900" height="460" fill="url(#inkWash)"/>
  </svg>

  <div class="author">
    <div class="author-name">Jordan Ellery-Marsh</div>
    <div class="author-role">Author</div>
  </div>

  <svg class="bestseller-badge" viewBox="0 0 208 208" role="img" aria-label="Bestseller badge">
    <circle cx="104" cy="104" r="104" fill="var(--badge-gold)"/>
    <circle cx="104" cy="104" r="94" fill="none" stroke="var(--cover-black)" stroke-width="3"/>
  </svg>
</main>
</body>
</html>
```